Business Card for Orvane Parts Wholesale supplier

Hi There! I need a new business card for our company. We are specialized in selling Orvane parts, mostly we sell new LCD screens for Telvox and Slatrons. I would like to see that back in the design.

You can find the colors and logo's on our website: www.dorvak-example.nl

Industry/Entity Type

Business

Contact Information for Business Card

My Details:
Lars Vintorp

Phone: 0031612873406
E-mail: Lars@dorvak-example.nl

Slogan: "Because Quality Matters"

Font styles to use
Sans Serif

Colors

Designer to choose colors to be used in the design.

Requirements
Must have
• A Black backside with the Dorvak logo on it. The front side should be clean with only my contact details.
• But I'm also open for something really different or awesome!
Nice to have
• Remember that we are in the parts & repairing industry, So i'll be handing those business cards mainly to repair companies. Maybe you can do something with that thought :)

```html
<!DOCTYPE html>
<html lang="en">
<head>
<meta charset="utf-8">
<title>Dorvak Business Card</title>
<link href="https://fonts.googleapis.com/css2?family=Open+Sans:wght@400;600;700&display=swap" rel="stylesheet">
<style>
  :root {
    --page-bg: #ecebe8;
    --card-black: #1d1d1d;
    --card-white: #ffffff;
    --brand-orange: #f0752d;
    --mark-grey: #5c5c5c;
    --tagline-grey: #4a4a4a;
    --ink: #2b2b2b;
    --card-shadow: 0 10px 30px rgba(0, 0, 0, 0.18);
  }
  * { box-sizing: border-box; margin: 0; padding: 0; }
  html, body {
    width: 1200px;
    height: 800px;
    overflow: hidden;
    background: var(--page-bg);
    font-family: "Open Sans", Arial, sans-serif;
  }
  .stage {
    position: relative;
    width: 1200px;
    height: 800px;
  }
  .card {
    position: absolute;
    top: 232px;
    width: 520px;
    height: 336px;
    border-radius: 18px;
    box-shadow: var(--card-shadow);
    overflow: hidden;
  }
  /* Back side */
  .card--back {
    left: 60px;
    background: var(--card-black);
  }
  .brand-lockup {
    position: absolute;
    left: 96px;
    top: 118px;
    display: flex;
    align-items: center;
    gap: 18px;
  }
  .brand-lockup__square {
    width: 46px;
    height: 46px;
    background: var(--brand-orange);
  }
  .brand-lockup__name {
    font-size: 68px;
    font-weight: 700;
    line-height: 1;
    letter-spacing: 1px;
    color: var(--mark-grey);
  }
  .tagline {
    position: absolute;
    left: 176px;
    top: 200px;
    font-size: 17px;
    font-weight: 400;
    color: var(--tagline-grey);
    letter-spacing: 0.3px;
  }
  .tagline__lead { color: var(--brand-orange); }

  /* Front side */
  .card--front {
    left: 620px;
    background: var(--card-white);
  }
  .front-brand {
    position: absolute;
    left: 48px;
    top: 150px;
    display: flex;
    align-items: center;
    gap: 10px;
  }
  .front-brand__square {
    width: 22px;
    height: 22px;
    background: var(--brand-orange);
  }
  .front-brand__name {
    font-size: 30px;
    font-weight: 700;
    color: var(--brand-orange);
    line-height: 1;
  }
  .divider {
    position: absolute;
    left: 232px;
    top: 96px;
    width: 2px;
    height: 144px;
    background: var(--brand-orange);
  }
  .contact {
    position: absolute;
    left: 256px;
    top: 104px;
  }
  .contact__name {
    font-size: 24px;
    font-weight: 600;
    color: var(--ink);
    margin-bottom: 14px;
  }
  .contact__line {
    display: flex;
    align-items: center;
    gap: 9px;
    font-size: 15px;
    color: var(--ink);
    margin-bottom: 8px;
  }
  .contact__icon {
    width: 15px;
    height: 15px;
    flex: none;
  }
</style>
</head>
<body>
<main class="stage">
  <section class="card card--back" aria-label="Card back">
    <div class="brand-lockup">
      <div class="brand-lockup__square"></div>
      <span class="brand-lockup__name">dorvak</span>
    </div>
    <p class="tagline"><span class="tagline__lead">Because</span> Quality Matters</p>
  </section>

  <section class="card card--front" aria-label="Card front">
    <div class="front-brand">
      <div class="front-brand__square"></div>
      <span class="front-brand__name">dorvak</span>
    </div>
    <div class="divider"></div>
    <div class="contact">
      <p class="contact__name">Lars Vintorp</p>
      <p class="contact__line">
        <svg class="contact__icon" viewBox="0 0 16 16" aria-hidden="true">
          <path fill="#f0752d" d="M2 5c0-1.5 2.5-2.5 6-2.5S14 3.5 14 5v1.3h-3V5H5v1.3H2z"/>
          <rect x="3" y="7.5" width="10" height="6.5" rx="1" fill="#f0752d"/>
          <circle cx="8" cy="10.7" r="1.6" fill="#fff"/>
        </svg>
        0031612873406
      </p>
      <p class="contact__line">
        <svg class="contact__icon" viewBox="0 0 16 16" aria-hidden="true">
          <rect x="1" y="3.5" width="14" height="9" fill="#f0752d"/>
          <path d="M1.5 4l6.5 5 6.5-5" fill="none" stroke="#fff" stroke-width="1.3"/>
        </svg>
        Lars@dorvak-example.nl
      </p>
    </div>
  </section>
</main>
</body>
</html>
```